Silver Creek Plumbing Business card & letter head design

We need a new business card and letter head for our plumbing company called silver creek plumbing. attached is the companys logo. We provide domestic and commercial plumbing services in regional western Australia. We are after Something simple yet nice to look at and something that fits within the trade industry.

Target Market(s)

trade/building industry

Contact Information for Business Card

Darl Hensby
Manager
0461 238 574
enquiries@scplumbwork.net.au
ABN: 47 381 905 462
PCL: 5187

Domestic & Commercial Plumbing
Tip Truck & Excavator hire

Colors

Designer to choose colors to be used in the design.

```html
<!DOCTYPE html>
<html lang="en">
<head>
<meta charset="utf-8">
<title>Silver Creek Plumbing – Business Card</title>
<link href="https://fonts.googleapis.com/css2?family=Montserrat:wght@600;700&family=Roboto:wght@300;400&display=swap" rel="stylesheet">
<style>
  :root {
    --brand-blue: #1257a8;
    --swoosh-grey: #55595e;
    --ink-grey: #555a5f;
    --paper: #ffffff;
    --backdrop: #e4e4e4;
  }
  * { margin: 0; padding: 0; box-sizing: border-box; }
  html, body {
    width: 1125px; height: 1200px; overflow: hidden;
    background: var(--backdrop);
  }
  .canvas { position: relative; width: 1125px; height: 1200px; }
  .card {
    position: absolute; left: 150px; width: 826px; height: 472px;
    border-radius: 26px; overflow: hidden;
  }
  .card--front { top: 98px; background: var(--paper); }
  .card--back { top: 632px; background: var(--brand-blue); }

  .wave { position: absolute; inset: 0; width: 100%; height: 100%; }

  .wordmark {
    position: absolute; font-family: "Montserrat", sans-serif; font-weight: 700;
    text-transform: uppercase; line-height: 1.05; letter-spacing: 0.5px;
  }
  .card--front .wordmark {
    left: 48px; top: 70px; color: var(--brand-blue); font-size: 40px;
  }
  .wordmark .line { display: block; }
  .wordmark .dot {
    display: inline-block; width: 22px; height: 22px; border-radius: 50%;
    background: currentColor; margin-left: 10px; vertical-align: middle;
  }

  .person { position: absolute; right: 32px; top: 42px; text-align: right; }
  .person__name {
    font-family: "Montserrat", sans-serif; font-weight: 700; font-size: 29px;
    color: var(--brand-blue); text-transform: uppercase; letter-spacing: 0.3px;
  }
  .person__role {
    font-family: "Roboto", sans-serif; font-weight: 400; font-size: 20px;
    color: var(--ink-grey); margin-top: 2px;
  }

  .contact, .registration {
    position: absolute; top: 375px; font-family: "Roboto", sans-serif;
    font-weight: 300; font-size: 21px; color: #fff; line-height: 27px;
  }
  .contact { left: 35px; }
  .contact li { list-style: none; display: flex; align-items: center; gap: 6px; }
  .contact svg { width: 18px; height: 18px; fill: #fff; }
  .registration { right: 44px; text-align: right; }

  .card--back .wordmark {
    left: 0; right: 0; top: 140px; text-align: center; color: #fff; font-size: 54px;
  }
  .tagline {
    position: absolute; left: 0; right: 0; top: 374px; text-align: center;
    font-family: "Roboto", sans-serif; font-weight: 300; font-size: 23px;
    color: #fff; line-height: 30px;
  }
</style>
</head>
<body>
<main class="canvas">
  <section class="card card--front">
    <svg class="wave" viewBox="0 0 826 472" preserveAspectRatio="none" aria-hidden="true">
      <path d="M0 315 C 200 260, 480 238, 680 243 C 500 245, 220 285, 0 352 Z" fill="var(--swoosh-grey)"/>
      <path d="M0 355 C 260 275, 560 235, 826 268 L 826 472 L 0 472 Z" fill="var(--brand-blue)"/>
    </svg>

    <div class="wordmark">
      <span class="line">Silver Creek<span class="dot"></span></span>
      <span class="line">Plumbing</span>
    </div>

    <div class="person">
      <div class="person__name">Darl Hensby</div>
      <div class="person__role">Manager</div>
    </div>

    <ul class="contact">
      <li>
        <svg viewBox="0 0 24 24" aria-hidden="true"><path d="M6.6 10.8a15.1 15.1 0 0 0 6.6 6.6l2.2-2.2c.3-.3.7-.4 1-.2 1.1.4 2.3.6 3.6.6.6 0 1 .4 1 1V20c0 .6-.4 1-1 1A17 17 0 0 1 3 4c0-.6.4-1 1-1h3.5c.6 0 1 .4 1 1 0 1.3.2 2.5.6 3.6.1.3 0 .7-.2 1z"/></svg>
        0461 238 574
      </li>
      <li>
        <svg viewBox="0 0 24 24" aria-hidden="true"><path d="M2 5h20v14H2z M2 5l10 8 10-8" fill="#fff" stroke="var(--brand-blue)" stroke-width="1.5"/></svg>
        enquiries@scplumbwork.net.au
      </li>
    </ul>

    <div class="registration">
      <div>ABN: 47 381 905 462</div>
      <div>PCL: 5187</div>
    </div>
  </section>

  <section class="card card--back">
    <div class="wordmark">
      <span class="line">Silver Creek<span class="dot"></span></span>
      <span class="line">Plumbing</span>
    </div>
    <p class="tagline">Domestic &amp; Commercial Plumbing<br>Tip Truck &amp; Excavator hire</p>
  </section>
</main>
</body>
</html>
```